Clinical psychologist - Psychotherapist business card

Hi everyone, I'm a clinical psychologist and psychotherapist, and I’m looking for a logo for my business card. The front will feature only the logo, while the back will include my contact details (and possibly a subtle touch of the logo). I've found two logos that I like, but the first one feels a bit childish—it lacks professionalism and doesn’t stand out from other similar designs. The second one, which I do like, unfortunately gives off a clinical, impersonal vibe.

Feel free to improvise—you don’t need to base the design on the logos I previously mentioned.

I generally prefer minimalistic designs that convey warmth, trust, and professionalism. I’d also like the card to have a bright background to make it feel inviting.

Additionally, I’m leaning toward using letterpress for the print technique, so the design should be compatible with that style—elegant, tactile, and clean. However, I’m still open to other options if they better suit the design.

UPDATE: I'm considering naming my business “Kalydo” (top-level domain: .gr), so you could incorporate that as well.

Target Market(s)

Psychology clients, Psychiatrists, Social media users

Industry/Entity Type

Clinical psychologist - Psychotherapist

Contact Information for Business Card

To be added later on

Colors

Designer to choose colors to be used in the design.

Requirements
Nice to have
• Possibly my initials on the front side. They are Δ Μ (capital letters) or δ μ (small letters).
Should not have
• Portraits of famous psychologists

```html
<!DOCTYPE html>
<html lang="en">
<head>
<meta charset="utf-8">
<title>Kalydo – Business Card</title>
<link rel="stylesheet" href="https://fonts.googleapis.com/css2?family=Poppins:wght@400;500;700&display=swap">
<style>
  :root {
    --backdrop: #777777;
    --paper-light: #fbfbfc;
    --paper-shade: #e6e8eb;
    --sky: #92cde3;
    --sky-deep: #7cbcd8;
    --line-tone: #c9ced4;
    --ink: #1d1d1d;
    --white: #ffffff;
  }
  * { margin: 0; padding: 0; box-sizing: border-box; }
  html, body {
    width: 993px; height: 1200px; overflow: hidden;
    background: var(--backdrop);
    font-family: "Poppins", sans-serif;
    color: var(--ink);
  }
  .card {
    position: absolute;
    width: 781px;
    overflow: hidden;
    background: linear-gradient(160deg, var(--paper-light) 0%, #f1f2f4 55%, var(--paper-shade) 100%);
  }
  .card--front { left: 106px; top: 142px; height: 430px; }
  .card--back  { left: 109px; top: 630px; height: 446px; }
  .card__art { position: absolute; inset: 0; width: 100%; height: 100%; }

  .card__flow {
    position: absolute;
    background: radial-gradient(ellipse at center, var(--line-tone) 0%, rgba(201,206,212,0.35) 45%, rgba(201,206,212,0) 72%);
  }
  .card--front .card__flow { right: -80px; bottom: -110px; width: 470px; height: 330px; }

  .brand { position: absolute; display: flex; flex-direction: column; align-items: center; }
  .brand__dot { border-radius: 50%; background: var(--sky); }
  .brand__name { font-weight: 500; color: var(--ink); line-height: 1; letter-spacing: 0.5px; white-space: nowrap; }
  .brand__tld { font-size: 0.45em; }

  .card--front .brand { left: 0; right: 0; top: 92px; }
  .card--front .brand__dot { width: 112px; height: 112px; margin-bottom: 14px; }
  .card--front .brand__name { font-size: 60px; }

  .card--back .brand { left: 28px; width: 300px; top: 160px; }
  .card--back .brand__dot { width: 88px; height: 88px; margin-bottom: 10px; }
  .card--back .brand__name { font-size: 46px; }

  .profile { position: absolute; left: 461px; top: 68px; width: 310px; }
  .profile__name { font-size: 29px; font-weight: 500; line-height: 1.2; white-space: nowrap; }
  .profile__name strong { font-weight: 700; }
  .profile__role { font-size: 17px; font-weight: 400; margin-top: 2px; }
  .profile__rule { position: relative; margin-top: 22px; width: 257px; height: 1px; background: #4a6b78; }
  .profile__rule::before { content: ""; position: absolute; left: 0; top: -1px; width: 34px; height: 3px; background: var(--white); }

  .contacts { list-style: none; margin-top: 26px; }
  .contacts__item { display: flex; align-items: center; gap: 13px; font-size: 19.5px; font-weight: 500; line-height: 1.32; margin-bottom: 18px; }
  .contacts__item--address { margin-bottom: 20px; }
  .contacts__icon {
    flex: none; width: 29px; height: 29px; border-radius: 50% 50% 50% 35%;
    background: var(--white); display: flex; align-items: center; justify-content: center;
  }
  .contacts__icon svg { width: 14px; height: 14px; fill: var(--ink); }
</style>
</head>
<body>

<section class="card card--front" aria-label="Card front">
  <div class="card__flow" role="img" aria-label="Flowing line decoration"></div>
  <div class="brand">
    <span class="brand__dot"></span>
    <span class="brand__name">Kalydo<span class="brand__tld">.gr</span></span>
  </div>
</section>

<section class="card card--back" aria-label="Card back">
  <svg class="card__art" viewBox="0 0 1368 780" preserveAspectRatio="none" aria-hidden="true">
    <defs>
      <linearGradient id="skyFill" x1="0" y1="0" x2="1" y2="1">
        <stop offset="0" stop-color="var(--sky)"/>
        <stop offset="1" stop-color="var(--sky-deep)"/>
      </linearGradient>
    </defs>
    <path fill="url(#skyFill)" d="M350,0 C365,70 470,130 560,190 C660,260 710,330 715,430 C720,520 650,560 645,640 C640,710 680,760 700,780 L1368,780 L1368,0 Z"/>
  </svg>

  <div class="brand">
    <span class="brand__dot"></span>
    <span class="brand__name">Kalydo<span class="brand__tld">.gr</span></span>
  </div>

  <div class="profile">
    <h1 class="profile__name"><strong>Nikos</strong> Arvanitis</h1>
    <p class="profile__role">Clinical psychologist</p>
    <div class="profile__rule"></div>
    <ul class="contacts">
      <li class="contacts__item contacts__item--address">
        <span class="contacts__icon"><svg viewBox="0 0 24 24"><path d="M12 2a7 7 0 0 0-7 7c0 5 7 13 7 13s7-8 7-13a7 7 0 0 0-7-7zm0 9.5A2.5 2.5 0 1 1 12 6.5a2.5 2.5 0 0 1 0 5z"/></svg></span>
        <span>Lorem Ipsum State,<br>Lorem Ipsum 875858</span>
      </li>
      <li class="contacts__item">
        <span class="contacts__icon"><svg viewBox="0 0 24 24"><path d="M6.6 10.8a15 15 0 0 0 6.6 6.6l2.2-2.2a1 1 0 0 1 1-.25 11.4 11.4 0 0 0 3.6.57 1 1 0 0 1 1 1V20a1 1 0 0 1-1 1A17 17 0 0 1 3 4a1 1 0 0 1 1-1h3.5a1 1 0 0 1 1 1c0 1.250.2 2.450.57 3.6a1 1 0 0 1-.25 1z"/></svg></span>
        <span>210 4418 2096</span>
      </li>
      <li class="contacts__item">
        <span class="contacts__icon"><svg viewBox="0 0 24 24"><path d="M3 5h18v14H3zm2 2v.5l7 5 7-5V7l-7 5z"/></svg></span>
        <span>info@kalydo.gr</span>
      </li>
      <li class="contacts__item">
        <span class="contacts__icon"><svg viewBox="0 0 24 24"><path d="M12 2a10 10 0 1 0 0 20 10 10 0 0 0 0-20zm6.9 6h-3a15 15 0 0 0-1.3-3.9A8 8 0 0 1 18.9 8zM12 4c.8 1.1 1.5 2.5 1.9 4h-3.8c.4-1.5 1.1-2.9 1.9-4zM4.3 14a8 8 0 0 1 0-4h3.4a16 16 0 0 0 0 4zm.8 2h3a15 15 0 0 0 1.3 3.9A8 8 0 0 1 5.1 16zm3-8h-3a8 8 0 0 1 4.3-3.9A15 15 0 0 0 8.1 8zM12 20c-.8-1.1-1.5-2.5-1.9-4h3.8c-.4 1.5-1.1 2.9-1.9 4zm2.3-6H9.7a14 14 0 0 1 0-4h4.6a14 14 0 0 1 0 4zm.3 5.9a15 15 0 0 0 1.3-3.9h3a8 8 0 0 1-4.3 3.9zM16.3 14a16 16 0 0 0 0-4h3.4a8 8 0 0 1 0 4z"/></svg></span>
        <span>www.kalydo.gr</span>
      </li>
    </ul>
  </div>
</section>

</body>
</html>
```